Restaurant menu design

Design fine dinning menu for Indian restaurant. Restaurant location is on river side. So if design has some touch of Yarra river of Melbourne and Indian touch. It is not compulsory. Creative and modern design is required.
I want to print in A3 and folded take away sizes so design should for both.
1. In A3, backside we need to design drink menu. I am attaching our current restaurant menu for drinks name and price.

Target Market(s)

Indian / Australian Customer

Industry/Entity Type

Indian Food, Indian fine dining

Colors
F0912C
F2A743
F7CA91
FBE8D2
FDF5EE

Requirements
Must have
• Simple but district design
Should not have
• common other restaurant type menu. Too many colours.

```html
<!DOCTYPE html>
<html lang="en">
<head>
<meta charset="utf-8">
<title>Tara's Table – Drinks Menu</title>
<link href="https://fonts.googleapis.com/css2?family=Italiana&family=Barlow+Condensed:wght@400;600&display=swap" rel="stylesheet">
<style>
  :root {
    --page-bg: #ffffff;
    --paper: #eeeeee;
    --paper-edge: #e2e2e2;
    --bronze: #75664b;
    --bronze-dark: #5f5139;
    --bronze-light: #8a7b60;
    --heading: #6b5b40;
    --ink: #1d1d1d;
    --ink-soft: #444444;
    --cream: #f3ede2;
    --rule: #7d7d7d;
    --rule-light: #d6cdb9;
  }
  * { box-sizing: border-box; margin: 0; padding: 0; }
  html, body { width: 1200px; height: 900px; overflow: hidden; background: var(--page-bg); }
  body { font-family: "Barlow Condensed", "Arial Narrow", sans-serif; color: var(--ink); }

  .trifold {
    position: absolute; left: 105px; top: 70px;
    width: 990px; height: 760px;
    display: flex;
    box-shadow: 0 18px 40px rgba(0,0,0,0.12);
  }
  .panel { position: relative; width: 330px; height: 100%; overflow: hidden; }
  .panel--light { background: var(--paper); }
  .panel--bronze {
    background: linear-gradient(180deg, var(--bronze-dark) 0%, var(--bronze-light) 45%, var(--bronze) 100%);
    color: var(--cream);
  }

  .section { position: absolute; left: 46px; right: 52px; }
  .section-title {
    font-family: "Italiana", "Didot", serif;
    font-size: 24px; font-weight: 400; line-height: 1;
    color: var(--heading); letter-spacing: 0.5px;
  }
  .panel--bronze .section-title { color: var(--cream); }
  .section-note { font-size: 9px; letter-spacing: 0.6px; color: var(--heading); margin-top: 3px; }
  .panel--bronze .section-note { color: var(--cream); opacity: .85; }

  .item-list { list-style: none; margin-top: 20px; }
  .item { margin-bottom: 11px; }
  .item-name { font-size: 7.5px; font-weight: 600; letter-spacing: 0.3px; text-transform: uppercase; }
  .item-row { display: flex; align-items: flex-end; gap: 5px; }
  .item-desc { font-size: 6.2px; color: var(--ink-soft); line-height: 1.3; max-width: 160px; }
  .panel--bronze .item-desc { color: var(--cream); opacity: .9; }
  .leader { flex: 1; border-bottom: 0.8px solid var(--rule); margin-bottom: 3px; min-width: 20px; }
  .panel--bronze .leader { border-color: var(--rule-light); }
  .price { font-size: 6.5px; white-space: nowrap; }

  .bev-list { list-style: none; margin-top: 14px; }
  .bev { display: flex; align-items: center; gap: 5px; margin-bottom: 6px; }
  .bev-name { font-size: 7.2px; font-weight: 600; text-transform: uppercase; white-space: nowrap; }
  .bev-name small { font-weight: 400; text-transform: none; font-size: 6px; margin-left: 4px; }
  .bev .price { font-size: 6px; }

  .beer-head { display: flex; align-items: flex-end; gap: 8px; }
  .beer-head .leader { margin-bottom: 5px; }
  .beer-head .price { font-size: 9px; letter-spacing: 0.4px; }
  .beer-list { list-style: none; margin-top: 14px; }
  .beer-list li { font-size: 7.5px; font-weight: 600; text-transform: uppercase; margin-bottom: 7px; }

  .brand {
    position: absolute; top: 160px; left: 0; right: 0; text-align: center;
    font-family: "Barlow Condensed", "Arial Narrow", sans-serif;
    font-weight: 600; font-size: 26px; color: var(--ink); letter-spacing: 0.2px;
  }
  .cover-title {
    position: absolute; top: 345px; left: 0; right: 0; text-align: center;
    font-family: "Italiana", "Didot", serif;
    font-size: 70px; color: var(--heading); font-weight: 400;
  }

  .riverscape { position: absolute; left: 0; right: 0; bottom: 0; }
  .riverscape--left { height: 195px; background: linear-gradient(180deg, rgba(238,238,238,0) 0%, #e2e2e2 40%, #dadada 100%); }
  .riverscape--mid { height: 280px; background: linear-gradient(180deg, rgba(117,102,75,0) 0%, rgba(80,68,48,0.55) 45%, rgba(70,60,42,0.7) 100%); }
  .riverscape--right { height: 300px; background: linear-gradient(180deg, rgba(238,238,238,0) 0%, #e4e4e4 45%, #dbdbdb 100%); }
</style>
</head>
<body>
  <main class="trifold">
    <section class="panel panel--light">
      <div class="section" style="top:92px">
        <h2 class="section-title">Mocktails</h2>
        <p class="section-note">(NON-ALCOHOLIC)</p>
        <ul class="item-list">
          <li class="item"><div class="item-name">Raspberry Crush</div><div class="item-row"><span class="item-desc">A vibrant and bubbly drink made with fresh raspberries</span><span class="leader"></span><span class="price">$10</span></div></li>
          <li class="item"><div class="item-name">Pina Colada</div><div class="item-row"><span class="item-desc" style="max-width:190px">A creamy and tropical delight made with coconut cream and pineapple juice</span><span class="leader"></span><span class="price">$12</span></div></li>
          <li class="item"><div class="item-name">Chilli Guava Cooler</div><div class="item-row"><span class="item-desc">A zesty and spicy drink made with guava</span><span class="leader"></span><span class="price">$10</span></div></li>
          <li class="item"><div class="item-name">Rose &amp; Lychee</div><div class="item-row"><span class="item-desc">A delicate and floral drink with fresh rose and lychee</span><span class="leader"></span><span class="price">$10</span></div></li>
          <li class="item"><div class="item-name">Mango Tango</div><div class="item-row"><span class="item-desc">Refreshing mango crush with sparkling orange juice</span><span class="leader"></span><span class="price">$10</span></div></li>
          <li class="item"><div class="item-name">Jaljeera Mojito</div><div class="item-row"><span class="item-desc">A tangy and minty drink with a classic twist</span><span class="leader"></span><span class="price">$12</span></div></li>
          <li class="item"><div class="item-name">Lychee &amp; Coconut</div><div class="item-row"><span class="item-desc">A creamy and exotic drink with lychee and coconut</span><span class="leader"></span><span class="price">$12</span></div></li>
        </ul>
      </div>

      <div class="section" style="top:350px; right:50px">
        <h2 class="section-title">Beverages</h2>
        <ul class="bev-list">
          <li class="bev"><span class="bev-name">Soft Drinks<small>(Cola/ Orange Soda/ Lemon Soda)</small></span><span class="leader"></span><span class="price">$4</span></li>
          <li class="bev"><span class="bev-name">Juices<small>(Apple/Orange)</small></span><span class="leader"></span><span class="price">$5</span></li>
          <li class="bev"><span class="bev-name">Volt Energy</span><span class="leader"></span><span class="price">$5</span></li>
          <li class="bev"><span class="bev-name">Mango Lassi</span><span class="leader"></span><span class="price">$6 GLASS $20 JUG</span></li>
          <li class="bev"><span class="bev-name">Masala Chaas</span><span class="leader"></span><span class="price">$5 GLASS $15 JUG</span></li>
          <li class="bev"><span class="bev-name">Dryfruit Lassi</span><span class="leader"></span><span class="price">$8 GLASS $25 JUG</span></li>
        </ul>
      </div>

      <div class="riverscape riverscape--left" role="img" aria-label="Line drawing of a riverside promenade with trees and low buildings"></div>
    </section>

    <section class="panel panel--bronze">
      <div class="section" style="top:82px; right:44px">
        <h2 class="section-title">Cocktails</h2>
        <p class="section-note">(ALCOHOLIC)</p>
        <ul class="item-list">
          <li class="item"><div class="item-name">The Bengal Tiger</div><div class="item-row"><span class="item-desc">A fiery and tropical blend of cherry and orange liquors, brandy and pineapple juice</span><span class="leader"></span><span class="price">$18</span></div></li>
          <li class="item"><div class="item-name">Jamuntini</div><div class="item-row"><span class="item-desc">A unique twist on the classic martini, featuring jamun dry gin, vermouth and a special masala blend for an exotic flavor profile</span><span class="leader"></span><span class="price">$18</span></div></li>
          <li class="item"><div class="item-name">Indian Winter</div><div class="item-row"><span class="item-desc">A comforting winter warmer with Indian whiskey, cardamom-infused honey and lemon juice for a soothing and spicy kick</span><span class="leader"></span><span class="price">$18</span></div></li>
          <li class="item"><div class="item-name">Sharabi Lassi</div><div class="item-row"><span class="item-desc">A decadent dessert drink with mango, coconut rum and a special spice mix for a tropical and indulgent experience</span><span class="leader"></span><span class="price">$18</span></div></li>
          <li class="item"><div class="item-name">Chilli Mango Margarita</div><div class="item-row"><span class="item-desc">A refreshing and spicy take on the classic margarita, with tequila, fresh mango and chili for a taste of summer</span><span class="leader"></span><span class="price">$18</span></div></li>
          <li class="item"><div class="item-name">Paan Mojito</div><div class="item-row"><span class="item-desc" style="max-width:200px">Experience taste of India with a twist with madira paan and madira select</span><span class="leader"></span><span class="price">$18</span></div></li>
        </ul>
      </div>

      <div class="section" style="top:366px; right:44px">
        <div class="beer-head"><h2 class="section-title">Beer</h2><span class="leader"></span><span class="price">$9 EACH BOTTLE</span></div>
        <ul class="beer-list">
          <li>Harbour Super Dry</li>
          <li>Sol Bay Extra</li>
          <li>Southern Reef Super Crisp Lager</li>
          <li>Riverstone Lager</li>
          <li>Pale Gold Blonde</li>
        </ul>
      </div>

      <div class="riverscape riverscape--mid" role="img" aria-label="Line drawing of a city skyline and arched bridge over the river"></div>
    </section>

    <section class="panel panel--light">
      <div class="brand">Tara's Table</div>
      <h1 class="cover-title">Menu</h1>
      <div class="riverscape riverscape--right" role="img" aria-label="Faint line drawing of a riverside skyline with trees and a winding river"></div>
    </section>
  </main>
</body>
</html>
```